Now Leasing Banner

Looking for a banner that says the following information approx 4' x 30'

Now Leasing Maplewood Terrace 925-318-6054

Target Market(s)

Drive by traffic

Industry/Entity Type

Residential property management

Requirements
Must have
• Clear and readable from a distance

```html
<!DOCTYPE html>
<html lang="en">
<head>
<meta charset="UTF-8">
<title>Now Leasing Banner – Maplewood Terrace</title>
<link rel="stylesheet" href="https://fonts.googleapis.com/css2?family=Bebas+Neue&display=swap">
<style>
  :root {
    --page-bg: #e9ecef;
    --banner-navy-deep: #14263a;
    --banner-navy: #1d3550;
    --banner-navy-light: #24405f;
    --text-white: #ffffff;
    --accent-line: #a9c8e6;
  }
  * { margin: 0; padding: 0; box-sizing: border-box; }
  html, body {
    width: 1200px;
    height: 800px;
    overflow: hidden;
    background: var(--page-bg);
  }
  .stage {
    position: relative;
    width: 1200px;
    height: 800px;
    display: flex;
    align-items: center;
    justify-content: center;
  }
  .leasing-banner {
    position: relative;
    width: 1120px;
    height: 150px;
    background: linear-gradient(135deg, var(--banner-navy-light) 0%, var(--banner-navy) 45%, var(--banner-navy-deep) 100%);
    overflow: hidden;
    box-shadow: 0 4px 14px rgba(0, 0, 0, 0.18);
  }
  .banner-graphics {
    position: absolute;
    inset: 0;
    width: 100%;
    height: 100%;
  }
  .headline {
    position: absolute;
    left: 150px;
    right: 60px;
    top: 56px;
    height: 56px;
    display: flex;
    align-items: center;
    font-family: "Bebas Neue", "Oswald", sans-serif;
    font-weight: 400;
    font-size: 58px;
    line-height: 1;
    letter-spacing: 0.5px;
    color: var(--text-white);
    text-transform: uppercase;
    white-space: nowrap;
  }
  .headline .phone { margin-left: 14px; }
</style>
</head>
<body>
  <main class="stage">
    <section class="leasing-banner" aria-label="Now Leasing Maplewood Terrace banner">
      <svg class="banner-graphics" viewBox="0 0 1120 150" aria-hidden="true">
        <g class="chevrons-lead" fill="none" stroke="var(--text-white)" stroke-width="4" stroke-linecap="square">
          <polyline points="44,18 53,27 44,36"/>
          <polyline points="57,18 66,27 57,36"/>
          <polyline points="70,18 79,27 70,36"/>
          <polyline points="83,18 92,27 83,36"/>
        </g>
        <g class="accent-lines" stroke="var(--accent-line)" stroke-width="2" fill="var(--accent-line)">
          <line x1="0" y1="48" x2="124" y2="48"/>
          <circle cx="126" cy="48" r="4" stroke="none"/>
          <line x1="0" y1="128" x2="1120" y2="128"/>
          <circle cx="160" cy="128" r="4" stroke="none"/>
          <circle cx="720" cy="128" r="4" stroke="none"/>
        </g>
        <g class="chevrons-trail" fill="none" stroke="var(--text-white)" stroke-width="2.5" stroke-linecap="square">
          <polyline points="1074,104 1068,110 1074,116"/>
          <polyline points="1082,104 1076,110 1082,116"/>
          <polyline points="1090,104 1084,110 1090,116"/>
          <polyline points="1098,104 1092,110 1098,116"/>
        </g>
      </svg>
      <h1 class="headline">Now Leasing Maplewood Terrace<span class="phone">925-318-6054</span></h1>
    </section>
  </main>
</body>
</html>
```